Business Card Design Project

I need a business card designed from scratch. I have an existing logo that I can upload in Illustrator for modification or redesign.

The Company is called Rank Harbor http://rankharbor.com.au and we provide Search Engine Optimization services to Australian businesses. The current logo signifies an increase in visitors, profits etc...

There are no restrictions as to the redesign - colours, style etc are all open to change.

Cards will be full colour and one sided printed at http://www.printlorvex.com.au so check their requirements for file format and sizes etc.

I will expect all original files upon completion of project.

Target Market(s)

Any business with a web site looking to improve their search engine rankings

Industry/Entity Type

Business

Requirements
Must have
• I like modern, sleek designs. Clean, not fussy, uncluttered.

```html
<!DOCTYPE html>
<html lang="en">
<head>
<meta charset="utf-8">
<title>Rank Harbor – Business Card</title>
<link rel="stylesheet" href="https://fonts.googleapis.com/css2?family=Arimo:wght@400;700&display=swap">
<style>
  :root {
    --page-bg: #8c8c8a;
    --card-white: #f7f9fd;
    --card-blue: #b9cdec;
    --card-blue-soft: #d6e2f5;
    --brand-blue: #2a6fc9;
    --band-yellow: #f4d314;
    --band-edge: #4a86d6;
    --ink: #111111;
    --icon-ink: #1d2a3a;
  }
  * { margin: 0; padding: 0; box-sizing: border-box; }
  html, body {
    width: 1200px;
    height: 750px;
    overflow: hidden;
  }
  body {
    background: var(--page-bg);
    font-family: "Arimo", Arial, sans-serif;
    display: flex;
    align-items: center;
    justify-content: center;
  }
  .business-card {
    position: relative;
    width: 404px;
    height: 660px;
    overflow: hidden;
    background:
      radial-gradient(ellipse 70% 30% at 35% 18%, var(--card-white) 0%, rgba(247,249,253,0) 100%),
      radial-gradient(ellipse 60% 25% at 55% 62%, var(--card-white) 0%, rgba(247,249,253,0) 100%),
      linear-gradient(160deg, var(--card-blue-soft) 0%, var(--card-blue) 45%, var(--card-blue-soft) 75%, var(--card-blue) 100%);
    box-shadow: 0 6px 18px rgba(0,0,0,0.25);
  }
  .brand {
    position: absolute;
    top: 52px;
    left: 30px;
    display: flex;
    align-items: center;
    gap: 12px;
  }
  .brand-dot {
    width: 22px;
    height: 22px;
    border-radius: 50%;
    background: var(--band-yellow);
  }
  .brand-name {
    font-weight: 700;
    font-size: 38px;
    color: var(--brand-blue);
    letter-spacing: -0.5px;
  }
  .name-band {
    position: absolute;
    top: 158px;
    left: 0;
    width: 100%;
    height: 66px;
    background: var(--band-yellow);
    border-bottom: 2px solid var(--band-edge);
    text-align: center;
    padding-top: 10px;
  }
  .person-name {
    font-size: 24px;
    color: var(--ink);
    line-height: 1.1;
  }
  .person-title {
    font-size: 14px;
    color: var(--brand-blue);
    margin-top: 3px;
  }
  .contact-list {
    position: absolute;
    right: 26px;
    bottom: 42px;
    list-style: none;
    text-align: right;
  }
  .contact-item {
    display: flex;
    align-items: center;
    justify-content: flex-end;
    gap: 6px;
    font-size: 21px;
    color: var(--ink);
    line-height: 1.28;
  }
  .contact-item svg { width: 17px; height: 17px; flex: none; }
</style>
</head>
<body>
  <main class="business-card">
    <div class="brand">
      <span class="brand-dot"></span>
      <span class="brand-name">Rank Harbor</span>
    </div>

    <div class="name-band">
      <p class="person-name">Liam Carver</p>
      <p class="person-title">Internet Marketing Consultant</p>
    </div>

    <ul class="contact-list">
      <li class="contact-item">
        <svg viewBox="0 0 24 24" aria-hidden="true"><path fill="var(--icon-ink)" d="M6.6 10.8a15.1 15.1 0 0 0 6.6 6.6l2.2-2.2c.3-.3.7-.4 1-.2 1.1.4 2.3.6 3.6.6.6 0 1 .4 1 1V20c0 .6-.4 1-1 1A17 17 0 0 1 3 4c0-.6.4-1 1-1h3.5c.6 0 1 .4 1 1 0 1.3.2 2.5.6 3.6.1.3 0 .7-.2 1z"/></svg>
        <span>1300 482915</span>
      </li>
      <li class="contact-item">
        <svg viewBox="0 0 24 24" aria-hidden="true"><rect x="2" y="5" width="20" height="14" fill="var(--icon-ink)"/><path d="M2 5l10 8 10-8" fill="none" stroke="#fff" stroke-width="1.6"/></svg>
        <span>liam@rankharbor.com.au</span>
      </li>
      <li class="contact-item">
        <svg viewBox="0 0 24 24" aria-hidden="true"><circle cx="12" cy="12" r="10" fill="var(--brand-blue)"/><path d="M2 12h20M12 2c3 3 3 17 0 20M12 2c-3 3-3 17 0 20" fill="none" stroke="#fff" stroke-width="1.2"/></svg>
        <span>www.rankharbor.com.au</span>
      </li>
    </ul>
  </main>
</body>
</html>
```